New School header and footer

Our school needs a modern new header and a matching footer. Currently we have the school logo, name and contact with no graphics at all (attached).
I have also attached another version of the school logo which is on our school sign.
The school's logo is a Swift (Apus pacificus) (bird) see http://www.findlyweb.example/search?q=swift+bird+images

The school is located in North Queensland Australia near the town of Ingham it was established in 1922

I would like the header/footer to have:
The school name- Marrelda State School
School moto - Courage beside kindness
contact details: Address Phone Fax website and principal email (some of these things could be in the footer) these details are in the uploaded files
The logo or elements of the logo (as is or modified to modernise)

School website is https://marreldass.qlx.edu.example

The header and footer would be used on A4 paper with microsoft word it will be used for the school newsletter and in all official school documents.

It can be colour or black and white. School uniforms are have light blue some dark blue and white the colours in the design are not limited to these colours.
Updates

Thanks to those people who have already submitted designs. I have made some additions to the brief in the should have and should not have sections and also the sliding scale thing. I hope that helps.

There are a lot of designs thankyou all so much. Some feedback from my staff is that we really need to keep the traditional logo of the bird from the website. It doesn't have to have the words around it but the shape and position needs to stay the same. I thought we were ready to change modernise the logo but unfortunately they aren't ready. However the rest of the design needs to be modern, less rigid and square. There is one square design that I did like and they have made the changes required. I will choose the designs I like and should be putting them up for online voting next week.
Just a side note a large tropical cyclone is moving close to our community. We are not at risk right now but it is possible that we will experience flooding and maybe loss of power so if there is a delay in posting the results this will probably be the reason.  I will try to respond to last minute questions or design submissions but I'll be pretty busy preparing my home and the school for the possibility of this weather event. Once again thankyou for your submissions I have been impressed by the quailty of the submissions from this particular design crowd.

Target Market(s)

For a school used in official documents, letters, and newsletters.

My staff will be choosing the winner.

Industry/Entity Type

School

Requirements
Must have
• School name
School motto
Address
Phone
Fax
Website URL
Header and footer
Should not have
• Avoid large amounts of block colours this letter head will be used in colour format most of the time but will be photo copied and faxed from time to time.

```html
<!DOCTYPE html>
<html lang="en">
<head>
<meta charset="utf-8">
<title>Marrelda State School Letterhead</title>
<link rel="stylesheet" href="https://fonts.googleapis.com/css2?family=Cormorant+Garamond:wght@600&family=PT+Sans&display=swap">
<style>
  :root {
    --navy: #26266a;
    --paper: #ffffff;
    --ink: #1f1f3f;
    --rule: #3a3a7a;
  }
  * { margin: 0; padding: 0; box-sizing: border-box; }
  html, body { width: 842px; height: 1200px; overflow: hidden; background: var(--paper); }
  .letterhead {
    position: relative;
    width: 842px;
    height: 1200px;
    background: var(--paper);
    overflow: hidden;
  }
  .band { position: absolute; left: 0; width: 842px; background: var(--navy); }
  .band--top { top: 0; height: 22px; }
  .band--bottom { bottom: 0; height: 24px; }

  .brand-mark {
    position: absolute;
    left: 36px;
    top: 38px;
    width: 70px;
    height: 70px;
    border-radius: 50%;
    background: var(--navy);
  }
  .school-name {
    position: absolute;
    left: 128px;
    top: 26px;
    font-family: "Cormorant Garamond", serif;
    font-weight: 600;
    font-size: 44px;
    line-height: 44px;
    color: var(--navy);
    text-transform: uppercase;
    letter-spacing: 1px;
    white-space: nowrap;
    transform: scaleX(0.55);
    transform-origin: left top;
  }
  .school-motto {
    position: absolute;
    left: 146px;
    top: 74px;
    font-family: "Cormorant Garamond", serif;
    font-weight: 600;
    font-size: 18px;
    color: var(--navy);
    text-transform: uppercase;
    letter-spacing: 1.5px;
    white-space: nowrap;
  }
  .contact-rule {
    position: absolute;
    left: 524px;
    top: 24px;
    width: 2px;
    height: 98px;
    background: var(--rule);
  }
  .contact-list {
    position: absolute;
    left: 534px;
    top: 27px;
    list-style: none;
    font-family: "PT Sans", sans-serif;
    font-size: 13.5px;
    line-height: 23px;
    color: var(--ink);
    white-space: nowrap;
  }
  .contact-list .phone,
  .contact-list .fax { padding-left: 2px; }
  .site-footer {
    position: absolute;
    left: 16px;
    top: 1134px;
    font-family: "PT Sans", sans-serif;
    font-size: 24px;
    color: var(--navy);
    white-space: nowrap;
  }
  .site-footer span { position: absolute; top: 0; }
  .site-footer .street { left: 0; }
  .site-footer .locality { left: 188px; }
  .site-footer .po-box { left: 370px; }
  .site-footer .postal-town { left: 526px; }
</style>
</head>
<body>
  <main class="letterhead">
    <div class="band band--top"></div>

    <header class="masthead">
      <div class="brand-mark" aria-hidden="true"></div>
      <h1 class="school-name">Marrelda State School</h1>
      <p class="school-motto">Courage beside kindness</p>
      <div class="contact-rule"></div>
      <ul class="contact-list">
        <li class="phone">Phone&nbsp; 4700 5318</li>
        <li class="fax">Fax 4700 5319</li>
        <li class="web">www.marreldass.qlx.edu.example</li>
        <li class="email">Email: theprincipal@marreldass.qlx.edu.example</li>
      </ul>
    </header>

    <footer class="site-footer">
      <span class="street">Coral Road</span>
      <span class="locality">Marrelda 4899</span>
      <span class="po-box">PO BOX 512</span>
      <span class="postal-town">KELVALE QLD 4899</span>
    </footer>

    <div class="band band--bottom"></div>
  </main>
</body>
</html>
```